Postcard: Open Sky Circle

Text for front: HOW TO CHANGE THE WORLD IN ONE [note: the word "one" should be underlined] STEPHint: It's up to you...[Note: add arrow or something to indicate "turn over"]Text for back: You're going to spend your entire life with someone you can never get away from. (Guess who?) Wouldn't you rather that person #OpenSkyCircle than judgmental or critical? BE the change you want to see! Visit www.OpenSkyCircle-hub.example for daily Dawn Pebbles and community. PLEASE JOIN US![Note: add logo to left half of back side]Font preference for text: Josefin sans

Target Market(s)

People who would be attracted to Corvane church - teravian perennist message. It's spiritual without being overtly religious, so the target market is probably early 30s and up but ideally won't turn off Millennials (folks under 30). It should attract attention of people who are open-minded and committed to progressive social change, tired of an atmosphere of hate-mongering and divisiveness.

Requirements
Nice to have
• It would be nice to convey a sense of challenge - there is an idea of "dawn pebbles" so something related to fire/sparks is appropriate. This is meant to evoke a deeper, divine love more than a sense of romantic love. This love is more fierce than fluffy! Yet it calls us to be our best selves.
Should not have
• Please avoid excessive pink - just the logo is enough, as this design needs to appeal to men as well as women.

```html
<!DOCTYPE html>
<html lang="en">
<head>
<meta charset="utf-8">
<title>Open Sky Circle — Postcard</title>
<link rel="stylesheet" href="https://fonts.googleapis.com/css2?family=Josefin+Sans:ital,wght@0,400;0,600;0,700;1,400&family=Marcellus+SC&family=Alfa+Slab+One&display=swap">
<style>
  :root {
    --page: #ffffff;
    --card: #5a3431;
    --card-edge: #4e2c29;
    --ink: #ffffff;
    --ink-soft: #f6eeee;
    --logo-tone: #e7668f;
    --shadow: rgba(0, 0, 0, 0.45);
  }
  * { box-sizing: border-box; margin: 0; padding: 0; }
  html, body {
    width: 895px; height: 1200px; overflow: hidden;
    background: var(--page);
  }
  .canvas { position: relative; width: 895px; height: 1200px; }

  .card {
    position: absolute; left: 29px; width: 804px;
    background: var(--card);
    box-shadow: 8px 10px 14px var(--shadow);
    color: var(--ink);
  }
  .card--front { top: 30px; height: 546px; }
  .card--back  { top: 589px; height: 547px; }

  /* Front */
  .headline {
    position: absolute; top: 52px; left: 0; width: 100%;
    text-align: center;
    font-family: "Marcellus SC", serif;
    font-size: 64px; line-height: 78px; letter-spacing: 3px;
  }
  .headline__one {
    font-family: "Alfa Slab One", serif;
    font-size: 56px; letter-spacing: 1px;
  }
  .turn-arrow {
    position: absolute; left: 338px; top: 286px; width: 170px; height: 130px;
  }
  .hint {
    position: absolute; top: 440px; left: 0; width: 100%;
    text-align: center;
    font-family: "Marcellus SC", serif;
    font-size: 36px; letter-spacing: 2px;
  }

  /* Back */
  .brand {
    position: absolute; left: 42px; top: 60px; width: 320px;
    display: flex; flex-direction: column; align-items: center; gap: 22px;
  }
  .brand__mark {
    width: 200px; height: 200px; border-radius: 50%;
    background: var(--logo-tone);
  }
  .brand__name {
    font-family: "Josefin Sans", sans-serif;
    font-weight: 600; font-size: 30px; color: var(--ink);
  }
  .message {
    position: absolute; left: 378px; top: 55px; width: 400px;
    font-family: "Josefin Sans", sans-serif;
    font-size: 21px; line-height: 30px; color: var(--ink-soft);
  }
  .message p { margin-bottom: 16px; }
  .message em { font-style: italic; }
  .visit {
    position: absolute; left: 360px; top: 352px; width: 430px;
    text-align: center;
    font-family: "Josefin Sans", sans-serif; color: var(--ink);
  }
  .visit__label { font-size: 21px; }
  .visit__url { font-size: 25px; font-weight: 700; margin-top: 10px; letter-spacing: 0.2px; }
  .visit__note { font-size: 21px; margin-top: 2px; }
  .join {
    position: absolute; left: 0; top: 470px; width: 100%;
    text-align: center;
    font-family: "Josefin Sans", sans-serif;
    font-size: 46px; letter-spacing: 0.5px; color: var(--ink);
  }
</style>
</head>
<body>
<main class="canvas">
  <section class="card card--front" aria-label="Postcard front">
    <h1 class="headline">How to change<br>the world in<br><span class="headline__one">ONE</span> step</h1>
    <svg class="turn-arrow" viewBox="0 0 170 130" aria-label="Turn over arrow" role="img">
      <defs>
        <filter id="glow" x="-30%" y="-30%" width="160%" height="160%">
          <feGaussianBlur stdDeviation="5" result="b"/>
          <feMerge><feMergeNode in="b"/><feMergeNode in="SourceGraphic"/></feMerge>
        </filter>
      </defs>
      <path filter="url(#glow)" fill="#f4f4f4"
        d="M40 8 C18 22 14 60 30 80 C42 95 70 98 112 96 L112 118 L160 80 L112 44 L112 66 C82 68 56 66 46 56 C36 44 34 26 40 8 Z"/>
    </svg>
    <p class="hint">Hint: It's up to you...</p>
  </section>

  <section class="card card--back" aria-label="Postcard back">
    <div class="brand">
      <span class="brand__mark" aria-hidden="true"></span>
      <span class="brand__name">Open Sky Circle</span>
    </div>
    <div class="message">
      <p>You're going to spend your entire life with someone you can never get away from. <em>(Guess who?)</em></p>
      <p>Wouldn't you rather that person #OpenSkyCircle than judgmental or critical?</p>
      <p>BE the change you want to see!</p>
    </div>
    <div class="visit">
      <div class="visit__label">Visit</div>
      <div class="visit__url">www.OpenSkyCircle-hub.example</div>
      <div class="visit__note">for daily Dawn Pebbles and community.</div>
    </div>
    <p class="join">PLEASE JOIN US</p>
  </section>
</main>
</body>
</html>
```